Startup Consultancy - Brochure Design

This needs to be a digital and potential hardcopy of a glossy brochure, designed to really catch the eye of prospective clients and draw them in. I am looking for something alternative from the "usual", but equally in keeping with the IT industry that the business operate in. The business specifically focuses on Print & Document Software and Technology solutions, and this should be considered in the design.

Target Market(s)

SMB and Corporate End Users, + Technology Resellers

Industry/Entity Type

Information Technology

Other font styles liked:
• Avenir

Colors
9d9d9d
848484
c3c3c3
e8e8e8
ffffff
eaeaea
0255a3
3176b5
85acd3

Requirements
Must have
• Company logo displayed on the front, plus any other relevant placements in pages
• Must follow the colour/style in some way of the website (www.brevantadvisory.co.uk)
Nice to have
• Some kind of infographical style in the brochure would be good, perhaps around the service listings

```html
<!DOCTYPE html>
<html lang="en">
<head>
<meta charset="utf-8">
<title>Brevant Consultancy – Brochure Spread</title>
<link rel="stylesheet" href="https://fonts.googleapis.com/css2?family=Arimo:wght@400;700&family=Roboto+Condensed:wght@400;700&display=swap">
<style>
  :root{
    --stage:#9d9d9d;
    --paper:#ffffff;
    --navy:#0255a3;
    --blue:#3176b5;
    --sky:#85acd3;
    --mist:#e8e8e8;
    --ink:#2b2b2b;
    --grey:#848484;
  }
  *{margin:0;padding:0;box-sizing:border-box}
  html,body{width:893px;height:1200px;overflow:hidden;background:var(--stage)}
  .spread{position:absolute;left:26px;top:303px;width:840px;height:594px;display:flex;box-shadow:0 6px 18px rgba(0,0,0,.25)}
  .panel{position:relative;width:420px;height:594px;background:var(--paper);overflow:hidden}
  .panel svg.shapes{position:absolute;inset:0;width:420px;height:594px}
  .heading{font-family:"Roboto Condensed",sans-serif;font-weight:700;color:var(--blue);font-size:17px;line-height:1}
  .subheading{font-family:"Arimo",sans-serif;color:var(--blue);font-size:9px;margin-top:3px}
  .body-copy{font-family:"Arimo",sans-serif;font-size:7.6px;line-height:10px;color:var(--ink);margin-top:8px}
  .about{position:absolute;left:30px;top:62px;width:360px}
  .photo-clearance{float:right;width:140px;height:140px;shape-outside:circle(94px at 55px 43px)}
  .why{position:absolute;left:30px;top:300px;width:355px}
  .brand{position:absolute;right:26px;top:24px;display:flex;align-items:center;gap:6px}
  .brand-mark{width:14px;height:14px;background:var(--ink)}
  .brand-name{font-family:"Roboto Condensed",sans-serif;font-weight:700;font-size:17px;color:var(--ink)}
  .contact{position:absolute;left:42px;top:380px}
  .contact h2{font-family:"Roboto Condensed",sans-serif;font-weight:700;font-size:17px;color:var(--ink)}
  .contact ul{list-style:none;margin-top:18px}
  .contact li{display:flex;align-items:flex-start;gap:10px;font-family:"Arimo",sans-serif;font-size:8.5px;line-height:11px;color:var(--ink);margin-bottom:13px}
  .contact svg{width:13px;height:13px;flex:none}
  .tagline{position:absolute;right:28px;top:408px;text-align:right;font-family:"Roboto Condensed",sans-serif;font-weight:700;color:var(--navy);font-size:36px;line-height:36px;letter-spacing:-.5px}
</style>
</head>
<body>
<main class="spread">
  <section class="panel panel-inside">
    <svg class="shapes" viewBox="0 0 420 594">
      <defs>
        <linearGradient id="networkTone" x1="0" y1="0" x2="1" y2="1">
          <stop offset="0" stop-color="#c3c3c3"/><stop offset=".6" stop-color="#6d86a3"/><stop offset="1" stop-color="#2d3f57"/>
        </linearGradient>
        <linearGradient id="phoneTone" x1="0" y1="0" x2="1" y2="1">
          <stop offset="0" stop-color="#f1b48a"/><stop offset=".6" stop-color="#d98a86"/><stop offset="1" stop-color="#8e6a8c"/>
        </linearGradient>
      </defs>
      <path class="footer-wave" d="M0,470 C120,440 260,520 420,455 V594 H0 Z" fill="var(--blue)"/>
      <circle cx="335" cy="105" r="84" fill="url(#networkTone)" stroke="var(--navy)" stroke-width="5" role="img" aria-label="Photo of business people beside a glowing digital network display"/>
      <circle cx="112" cy="515" r="66" fill="url(#phoneTone)" stroke="var(--navy)" stroke-width="5" role="img" aria-label="Photo of hands holding a smartphone"/>
    </svg>
    <div class="about">
      <div class="photo-clearance" aria-hidden="true"></div>
      <h2 class="heading">About Us</h2>
      <p class="subheading">Taking a different path</p>
      <p class="body-copy">We provide services to End User organisations of all sizes, ranging from SMB through to Enterprise and Government, across a wide range of vertical markets. We help clients plan forward thinking print and document workflows, bringing an independent view that is free of any vendor ties. Our team also supports resellers and channel partners with strategy, design and delivery services built around their own customers. With many years spent inside the print and document industry, our consultants combine technical depth with honest, practical advice. We do not sell hardware or software, and we are not bound to any manufacturer or distributor. What we offer is trusted, impartial consultancy, design and advice.</p>
    </div>
    <div class="why">
      <h2 class="heading">Why Choose Us?</h2>
      <p class="subheading">How do we do that?</p>
      <p class="body-copy">Honest and open advice, with full transparency in our approach and integrity in everything we recommend. If a solution is not right for you, we will tell you so openly, with no fuss and no over promising. Our consultancy services also make sure you are aware of and prepared for the potential pitfalls, complexities and challenges found in the world of Print &amp; Document solutions.</p>
    </div>
  </section>

  <section class="panel panel-cover">
    <svg class="shapes" viewBox="0 0 420 594">
      <defs>
        <linearGradient id="teamTone" x1="0" y1="0" x2="1" y2="1">
          <stop offset="0" stop-color="#e8e8e8"/><stop offset=".45" stop-color="#85acd3"/><stop offset="1" stop-color="#3b4b63"/>
        </linearGradient>
      </defs>
      <path d="M0,540 C90,520 150,560 230,594 H0 Z" fill="var(--blue)"/>
      <path d="M30,0 H420 V235 C360,320 220,345 120,300 C55,270 25,150 30,0 Z" fill="url(#teamTone)" role="img" aria-label="Photo of two IT professionals reviewing a laptop in a server room"/>
      <path d="M420,250 C360,335 215,360 110,312 C45,282 14,160 18,40" fill="none" stroke="var(--navy)" stroke-width="6"/>
    </svg>
    <div class="brand">
      <span class="brand-mark"></span>
      <span class="brand-name">Brevant</span>
    </div>
    <div class="contact">
      <h2>Contact Us</h2>
      <ul>
        <li><svg viewBox="0 0 14 14"><circle cx="7" cy="7" r="6.3" fill="none" stroke="var(--navy)" stroke-width="1.2"/><path d="M4.6 3.8l1.3 1.4-.7.9c.5 1 1.1 1.6 2.1 2.1l.9-.7 1.4 1.3-.8 1c-2.4-.3-4.7-2.6-5-5z" fill="var(--navy)"/></svg>0203 555 0182</li>
        <li><svg viewBox="0 0 14 14"><circle cx="7" cy="7" r="6.3" fill="none" stroke="var(--navy)" stroke-width="1.2"/><rect x="3.8" y="4.8" width="6.4" height="4.4" fill="var(--navy)"/><path d="M3.8 4.8L7 7.3l3.2-2.5" fill="none" stroke="#fff" stroke-width=".8"/></svg>enquiries@brevantadvisory.co.uk</li>
        <li><svg viewBox="0 0 14 14"><circle cx="7" cy="7" r="6.3" fill="none" stroke="var(--navy)" stroke-width="1.2"/><path d="M7 3.3a2.4 2.4 0 0 1 2.4 2.4C9.4 7.5 7 10.6 7 10.6S4.6 7.5 4.6 5.7A2.4 2.4 0 0 1 7 3.3z" fill="var(--navy)"/><circle cx="7" cy="5.7" r=".9" fill="#fff"/></svg><span>48 Calder Row,<br>London,<br>WC1X 4PL</span></li>
      </ul>
    </div>
    <p class="tagline">You Dream IT<br>We Build IT</p>
  </section>
</main>
</body>
</html>
```